Designing a billboard

Should have
Corwell & Pine, LLC
Ph: 512-647-3918
Auto Accidents / Personal Injury
Family Law
Criminal Defense
Real Estate
Free Consultation

Target Market(s)

Legal

Industry/Entity Type

Legal

Font styles to use
Serif
Sans Serif

Requirements
Must have
• Designing a billboard

Should have
Corwell & Pine, LLC
Ph: 512-647-3918
Family Law
Criminal Defense
Real Estate
Free Consultation
Nice to have
• Nice to have info above
Should not have
• None

```html
<!DOCTYPE html>
<html lang="en">
<head>
<meta charset="utf-8">
<title>Corwell &amp; Pine, LLC — Billboard</title>
<link rel="stylesheet" href="https://fonts.googleapis.com/css2?family=Cinzel:wght@700&family=Oswald:wght@300;500;600&display=swap">
<style>
  :root {
    --navy-deep: #000f2e;
    --navy-mid: #002b5c;
    --navy-gap: #001a40;
    --photo-blue: #0a4f8f;
    --band-blue: #0c8bd6;
    --white: #ffffff;
  }
  * { margin: 0; padding: 0; box-sizing: border-box; }
  html, body { width: 1200px; height: 1200px; overflow: hidden; background: var(--navy-gap); }
  .billboard { position: relative; width: 1200px; height: 1200px; background: var(--navy-gap); }

  .header {
    position: absolute; left: 0; top: 0; width: 1200px; height: 412px;
    background: var(--navy-deep);
  }
  .header-photo {
    position: absolute; inset: 0;
    background:
      radial-gradient(ellipse 55% 70% at 40% 35%, rgba(20,110,190,0.75) 0%, rgba(10,79,143,0.45) 40%, rgba(0,15,46,0) 75%),
      linear-gradient(120deg, var(--navy-deep) 0%, #02234f 45%, var(--navy-deep) 80%);
  }
  .firm-name {
    position: absolute; left: 0; right: 0; top: 38px;
    font-family: "Cinzel", "Times New Roman", serif; font-weight: 700;
    color: var(--white); text-align: center;
    font-size: 128px; line-height: 154px; letter-spacing: 1px;
  }

  .practice-band {
    position: absolute; left: 0; width: 1200px; height: 104px;
    background: var(--band-blue);
    display: flex; align-items: center; justify-content: center;
    font-family: "Oswald", "Arial Narrow", sans-serif; font-weight: 600;
    color: var(--white); font-size: 72px; letter-spacing: -0.5px; text-transform: uppercase;
  }
  .band-1 { top: 412px; }
  .band-2 { top: 536px; }
  .band-3 { top: 657px; }
  .band-4 { top: 778px; }

  .contact {
    position: absolute; left: 0; top: 882px; width: 1200px; height: 318px;
    background: var(--navy-mid); color: var(--white); text-align: center;
    font-family: "Oswald", "Arial Narrow", sans-serif;
  }
  .contact-invite {
    margin-top: 44px; font-size: 56px; line-height: 1; font-weight: 300;
    text-transform: uppercase; letter-spacing: 1px;
  }
  .contact-invite strong { font-weight: 500; }
  .contact-phone {
    margin-top: 20px; font-size: 168px; line-height: 1; font-weight: 600; letter-spacing: -1px;
  }
</style>
</head>
<body>
  <main class="billboard">
    <section class="header">
      <div class="header-photo" role="img" aria-label="Dark blue close-up photo of a judge's gavel"></div>
      <h1 class="firm-name">Corwell &amp;<br>Pine, LLC</h1>
    </section>

    <div class="practice-band band-1">Auto Accidents / Personal Injury</div>
    <div class="practice-band band-2">Family Law</div>
    <div class="practice-band band-3">Criminal Defense</div>
    <div class="practice-band band-4">Real Estate</div>

    <section class="contact">
      <p class="contact-invite">For <strong>Free Consultation</strong> call us at</p>
      <p class="contact-phone">512-647-3918</p>
    </section>
  </main>
</body>
</html>
```